Finance Product Agency Business Card Design

We're an agency that provides products (service contracts, gap insurance, tire and wheel, etc) and support to dealership finance departments. We specialize in training finance producers to maximize their potential and also keep them up to date on the ever changing compliance and legal landscape. I'll attach an image of our logo, excited to see what you all come up with. Would also be interested in discussing our new website design with the winner.

Target Market(s)

auto dealerships

Industry/Entity Type

Business

Contact Information for Business Card

Mark Dolvery
Phone 317.624.5583
Fax 855.472.3308
email Mark.Dolvery@brightlanecoverage.example

Requirements
Must have
• basic contact information
Nice to have
• looking for something professional but modern

```html
<!DOCTYPE html>
<html lang="en">
<head>
<meta charset="utf-8">
<title>Brightlane Coverage – Business Card</title>
<link rel="stylesheet" href="https://fonts.googleapis.com/css2?family=Open+Sans:wght@400;700;800&display=swap">
<style>
  :root {
    --page-bg: #e6e8ea;
    --card-white: #f7f7f6;
    --teal: #4a7589;
    --teal-light: #5b889c;
    --teal-dark: #3a6275;
    --swoosh-dark: #1d272d;
    --ink-white: #ffffff;
    --brand-ink: #3e6679;
  }
  * { margin: 0; padding: 0; box-sizing: border-box; }
  html, body { width: 1200px; height: 780px; overflow: hidden; }
  body {
    background: var(--page-bg);
    font-family: "Open Sans", Arial, sans-serif;
    position: relative;
  }
  .card {
    position: absolute;
    top: 230px;
    width: 560px;
    height: 320px;
    overflow: hidden;
    box-shadow: 0 6px 18px rgba(0,0,0,0.18);
  }
  .card-front { left: 25px; background: var(--card-white); }
  .card-back {
    left: 615px;
    background: radial-gradient(ellipse at 45% 40%, var(--teal-light) 0%, var(--teal) 50%, var(--teal-dark) 100%);
  }
  .card-art { position: absolute; inset: 0; width: 560px; height: 320px; }

  .brand {
    position: absolute;
    display: flex;
    align-items: center;
    gap: 14px;
  }
  .brand-dot { width: 44px; height: 44px; border-radius: 50%; flex: none; }
  .brand-name {
    font-weight: 800;
    text-transform: uppercase;
    line-height: 1.02;
    letter-spacing: 0.5px;
  }
  .card-front .brand { left: 34px; top: 78px; }
  .card-front .brand-dot { background: var(--brand-ink); }
  .card-front .brand-name { color: var(--brand-ink); font-size: 30px; }

  .card-back .brand {
    left: 0; right: 0; top: 0; bottom: 0;
    justify-content: center;
    gap: 20px;
  }
  .card-back .brand-dot { width: 60px; height: 60px; background: var(--ink-white); }
  .card-back .brand-name { color: var(--ink-white); font-size: 40px; }

  .contact {
    position: absolute;
    left: 298px;
    top: 190px;
    color: var(--ink-white);
  }
  .contact-name { font-size: 20px; font-weight: 700; margin-bottom: 8px; white-space: nowrap; }
  .contact-line {
    display: flex;
    align-items: center;
    gap: 6px;
    font-size: 11px;
    line-height: 22px;
    white-space: nowrap;
  }
  .contact-icon {
    width: 12px; height: 12px;
    background: var(--ink-white);
    border-radius: 2px;
    display: flex; align-items: center; justify-content: center;
    flex: none;
  }
  .contact-icon svg { width: 9px; height: 9px; }
</style>
</head>
<body>

<section class="card card-front" aria-label="Business card front">
  <svg class="card-art" viewBox="0 0 560 320" aria-hidden="true">
    <defs>
      <linearGradient id="band-fill" x1="0" y1="1" x2="1" y2="0">
        <stop offset="0" stop-color="#3f687b"/>
        <stop offset="0.5" stop-color="#4f7d91"/>
        <stop offset="1" stop-color="#3c6376"/>
      </linearGradient>
      <linearGradient id="swoosh-fill" x1="0" y1="1" x2="1" y2="0">
        <stop offset="0" stop-color="#2a3a42"/>
        <stop offset="1" stop-color="#141b1f"/>
      </linearGradient>
    </defs>
    <path class="swoosh-shadow" fill="url(#swoosh-fill)"
          d="M420 0 C322 30 282 120 268 200 C254 262 224 302 178 320 L190 320 C240 300 270 260 285 205 C305 125 355 30 475 0 Z"/>
    <path class="colour-band" fill="url(#band-fill)"
          d="M190 320 C240 300 270 260 285 205 C305 125 355 30 475 0 L560 0 L560 320 Z"/>
    <path class="band-highlight" fill="none" stroke="rgba(255,255,255,0.55)" stroke-width="1.2"
          d="M205 320 C252 302 280 266 296 212"/>
  </svg>

  <div class="brand">
    <span class="brand-dot"></span>
    <span class="brand-name">Brightlane<br>Coverage</span>
  </div>

  <div class="contact">
    <p class="contact-name">Mark Dolvery</p>
    <p class="contact-line">
      <span class="contact-icon">
        <svg viewBox="0 0 10 10"><path fill="#4a7589" d="M2 1 L4 1 L4.6 3 L3.4 3.8 C4 5 5 6 6.2 6.6 L7 5.4 L9 6 L9 8 C9 8.6 8.6 9 8 9 C4.2 9 1 5.8 1 2 C1 1.4 1.4 1 2 1 Z"/></svg>
      </span>317.624.5583
    </p>
    <p class="contact-line">
      <span class="contact-icon">
        <svg viewBox="0 0 10 10"><rect x="2.5" y="1" width="5" height="3" fill="#4a7589"/><rect x="1" y="4" width="8" height="4" rx="0.8" fill="#4a7589"/><rect x="2.5" y="7" width="5" height="2" fill="#4a7589"/></svg>
      </span>855.472.3308
    </p>
    <p class="contact-line">
      <span class="contact-icon">
        <svg viewBox="0 0 10 10"><rect x="1" y="2.2" width="8" height="5.6" fill="none" stroke="#4a7589" stroke-width="1.1"/><path d="M1 2.4 L5 5.6 L9 2.4" fill="none" stroke="#4a7589" stroke-width="1.1"/></svg>
      </span>Mark.Dolvery@brightlanecoverage.example
    </p>
  </div>
</section>

<section class="card card-back" aria-label="Business card back">
  <div class="brand">
    <span class="brand-dot"></span>
    <span class="brand-name">Brightlane<br>Coverage</span>
  </div>
</section>

</body>
</html>
```